Business cards for a high-end menswear store

I would like to come up with a design for our business cards.
Two different ones: one for general sales and one for the owner. It is a high-end menswear store.

Our address is: 4817 Valmonde Boulevard, Montreal, QC, H2R4K7
phone number: 514-582-3960
insta: MAISONVERLAINT
Website: www.maisonverlaint.com
email (general card): info@maisonverlaint.com
email (owner): morvin@maisonverlaint.com

I have attached our logo in an ai and eps file format. You can see our old cards as well. I am looking for a modern and clean look.

Target Market(s)

High-End Clothing Market

Industry/Entity Type

Retail, Clothing, Luxury Clothing

Contact Information for Business Card

Address, Name, Email, Website, Social Info,

Font styles to use
Serif

Colors

Designer to choose colors to be used in the design.

Requirements
Must have
• Address, Name, Email, Website, Social Info,
Nice to have
• QR Code that brings you to the website

```html
<!DOCTYPE html>
<html lang="en">
<head>
<meta charset="utf-8">
<title>Maison Verlaint – Business Cards</title>
<link rel="stylesheet" href="https://fonts.googleapis.com/css2?family=Poppins:wght@400;500;600;700&display=swap">
<style>
  :root {
    --page-bg: #ece8e3;
    --card-bg: #232122;
    --ink-light: #ffffff;
    --ink-dark: #232122;
    --card-shadow: rgba(0, 0, 0, 0.22);
  }
  * { box-sizing: border-box; margin: 0; padding: 0; }
  html, body {
    width: 1200px;
    height: 1200px;
    overflow: hidden;
    background: var(--page-bg);
    font-family: "Poppins", sans-serif;
    color: var(--ink-light);
  }
  .canvas {
    position: relative;
    width: 1200px;
    height: 1200px;
  }
  .card {
    position: absolute;
    left: 180px;
    width: 840px;
    height: 500px;
    background: var(--card-bg);
    border-radius: 38px;
    box-shadow: 0 18px 40px var(--card-shadow);
  }
  .card--front { top: 70px; }
  .card--back { top: 630px; }

  /* Brand name block (front) */
  .brand {
    position: absolute;
    display: flex;
    align-items: center;
    gap: 14px;
    font-weight: 500;
    letter-spacing: 0.22em;
    color: var(--ink-light);
    text-transform: uppercase;
  }
  .brand__square {
    flex: none;
    background: var(--ink-light);
  }
  .brand__name { line-height: 1.35; }

  .card--front .brand { left: 70px; top: 212px; }
  .card--front .brand__square { width: 22px; height: 22px; }
  .card--front .brand__name { font-size: 20px; }

  /* Holder */
  .holder {
    position: absolute;
    left: 360px;
    top: 92px;
  }
  .holder__first {
    font-size: 28px;
    font-weight: 400;
    line-height: 1.15;
    letter-spacing: 0.02em;
  }
  .holder__last {
    font-size: 28px;
    font-weight: 700;
    line-height: 1.15;
    letter-spacing: 0.02em;
  }
  .holder__role {
    margin-top: 4px;
    font-size: 9px;
    font-weight: 600;
    letter-spacing: 0.2em;
  }

  /* Contact list */
  .contacts {
    position: absolute;
    left: 360px;
    top: 212px;
    list-style: none;
  }
  .contact {
    display: flex;
    align-items: center;
    gap: 14px;
    height: 40px;
    margin-bottom: 24px;
    font-size: 17px;
    font-weight: 500;
    line-height: 1.3;
  }
  .contact--address { align-items: flex-start; height: auto; }
  .contact__icon {
    flex: none;
    width: 26px;
    height: 26px;
  }

  /* Back */
  .card--back .brand {
    left: 0;
    right: 0;
    top: 175px;
    justify-content: center;
    gap: 24px;
  }
  .card--back .brand__square { width: 40px; height: 40px; }
  .card--back .brand__name { font-size: 42px; }

  .social {
    position: absolute;
    left: 70px;
    bottom: 62px;
    display: flex;
    align-items: center;
    gap: 14px;
    font-size: 17px;
    font-weight: 500;
    letter-spacing: 0.02em;
  }
  .social__mark {
    width: 30px;
    height: 30px;
    border: 2.5px solid var(--ink-light);
    border-radius: 7px;
  }
</style>
</head>
<body>
<main class="canvas">

  <section class="card card--front" aria-label="Business card front">
    <div class="brand">
      <span class="brand__square"></span>
      <span class="brand__name">Maison<br>Verlaint</span>
    </div>

    <div class="holder">
      <p class="holder__first">NAME</p>
      <p class="holder__last">SURNAME</p>
      <p class="holder__role">CEO</p>
    </div>

    <ul class="contacts">
      <li class="contact">
        <svg class="contact__icon" viewBox="0 0 26 26" aria-hidden="true">
          <circle cx="13" cy="13" r="13" fill="#fff"/>
          <g fill="none" stroke="#232122" stroke-width="1.4">
            <circle cx="13" cy="13" r="7"/>
            <ellipse cx="13" cy="13" rx="3" ry="7"/>
            <line x1="6" y1="13" x2="20" y2="13"/>
          </g>
        </svg>
        <span>www.maisonverlaint.com</span>
      </li>
      <li class="contact">
        <svg class="contact__icon" viewBox="0 0 26 26" aria-hidden="true">
          <circle cx="13" cy="13" r="13" fill="#fff"/>
          <rect x="6.5" y="8.5" width="13" height="9" rx="1" fill="#232122"/>
          <polyline points="7,9.5 13,14 19,9.5" fill="none" stroke="#fff" stroke-width="1.3"/>
        </svg>
        <span>info@maisonverlaint.com</span>
      </li>
      <li class="contact">
        <svg class="contact__icon" viewBox="0 0 26 26" aria-hidden="true">
          <circle cx="13" cy="13" r="13" fill="#fff"/>
          <path d="M9 6.5l2.6 0.2 1.1 3.2-1.6 1.3c0.8 1.7 2 2.9 3.7 3.7l1.3-1.6 3.2 1.1 0.2 2.6c-0.7 1-2 1.6-3.2 1.4C11.4 17.6 8.4 14.6 7.6 9.7 7.4 8.5 8 7.2 9 6.5z" fill="#232122"/>
        </svg>
        <span>514-582-3960</span>
      </li>
      <li class="contact contact--address">
        <svg class="contact__icon" viewBox="0 0 26 26" aria-hidden="true">
          <circle cx="13" cy="13" r="13" fill="#fff"/>
          <path d="M13 5.5c-3 0-5.2 2.2-5.2 5.1 0 3.6 5.2 9.4 5.2 9.4s5.2-5.8 5.2-9.4c0-2.9-2.2-5.1-5.2-5.1z" fill="#232122"/>
          <circle cx="13" cy="10.6" r="1.9" fill="#fff"/>
        </svg>
        <span>4817 Valmonde Boulevard,<br>Montreal, QC, H2R4K7</span>
      </li>
    </ul>
  </section>

  <section class="card card--back" aria-label="Business card back">
    <div class="brand">
      <span class="brand__square"></span>
      <span class="brand__name">Maison<br>Verlaint</span>
    </div>

    <div class="social">
      <span class="social__mark" aria-hidden="true"></span>
      <span>MAISONVERLAINT</span>
    </div>
  </section>

</main>
</body>
</html>
```